Stationary Design For New Dynamic Company

Hi there we require stationary designed for our new company, we have used "Sketch Meadow" recently for our logo and were very impressed with all of the designers that contributed towards the final result.
What we require now is the following:
Letter head layout (A4)
Business Cards (5 people)
With Compliments slips
Envelopes
Email stationary
We would like to use our current logo design and I have included it for your use (JPEG is the one we have chosen and I have attached an EPS file for your use). Our company specializes in architectural cladding and our products are used by architects, builders and private clients, so we wish for the stationary to be suitable and attractive to our clientele.
I thank everyone in advance for your contributions.
Thank you to all that have provided your designs for this project, I apologize for not providing feedback as I have been away. I have looked at everyone's designs and they all look great and I will come back to those designers that I wish to have changes made sometime today.
Once again a big thank you to all involved.

```html
<!DOCTYPE html>
<html lang="en">
<head>
<meta charset="utf-8">
<title>NOVACLAD Stationery</title>
<link href="https://fonts.googleapis.com/css2?family=Open+Sans:wght@400;700&display=swap" rel="stylesheet">
<style>
  :root {
    --navy: #2b2f73;
    --orange: #f58220;
    --ink: #1e1e1e;
    --paper: #ffffff;
    --bg-top: #a8a8a8;
    --bg-bottom: #383838;
    --shadow: 3px 4px 7px rgba(0, 0, 0, 0.6);
  }
  * { margin: 0; padding: 0; box-sizing: border-box; }
  html, body { width: 1200px; height: 900px; overflow: hidden; }
  body {
    font-family: "Open Sans", Arial, sans-serif;
    color: var(--ink);
  }
  .board {
    position: relative;
    width: 1200px;
    height: 900px;
    background: linear-gradient(to bottom, var(--bg-top), var(--bg-bottom));
  }
  .sheet, .card {
    position: absolute;
    background: var(--paper);
    box-shadow: var(--shadow);
    overflow: hidden;
  }
  .brand {
    position: absolute;
    display: flex;
    align-items: center;
    gap: 8px;
    font-weight: 700;
    color: var(--navy);
    letter-spacing: -0.5px;
    white-space: nowrap;
  }
  .brand-square {
    background: var(--orange);
    display: block;
  }
  .edge-band {
    position: absolute;
    left: 0;
    right: 0;
    bottom: 0;
    background: var(--orange);
  }
  .web { color: var(--orange); white-space: nowrap; }

  /* Letterhead */
  .letterhead { left: 465px; top: 33px; width: 542px; height: 767px; }
  .letterhead .brand { left: 22px; top: 50px; font-size: 28px; }
  .letterhead .brand-square { width: 20px; height: 20px; }
  .letterhead .address {
    position: absolute; right: 19px; top: 34px;
    font-style: normal; text-align: right; font-size: 11px; line-height: 14px;
  }
  .letterhead .web { position: absolute; right: 19px; top: 99px; font-size: 11px; }
  .letterhead .edge-band { height: 8px; }

  /* Business card front */
  .card-front { left: 339px; top: 232px; width: 223px; height: 120px; }
  .card-front .brand { left: 8px; top: 11px; font-size: 13px; gap: 4px; }
  .card-front .brand-square { width: 9px; height: 9px; }
  .card-front .details {
    position: absolute; right: 7px; top: 7px;
    text-align: right; font-size: 6px; line-height: 8.5px;
  }
  .card-front .details .gap { height: 8px; }
  .card-front .web { position: absolute; right: 7px; bottom: 11px; font-size: 6px; }
  .card-front .edge-band { height: 4px; }

  /* Business card back */
  .card-back { left: 339px; top: 388px; width: 223px; height: 120px; }
  .card-back .products {
    position: absolute; right: 7px; bottom: 8px;
    list-style: none; text-align: right; font-size: 8.5px; line-height: 11.5px;
  }
  .card-back .edge-band { height: 4px; }
</style>
</head>
<body>
<main class="board">

  <section class="sheet letterhead" aria-label="Letterhead">
    <div class="brand"><span class="brand-square"></span>NOVACLAD</div>
    <address class="address">
      01234567890<br>1 Street Address<br>Yourcity<br>1234
    </address>
    <div class="web">www.novaclad.com</div>
    <div class="edge-band"></div>
  </section>

  <section class="card card-front" aria-label="Business card front">
    <div class="brand"><span class="brand-square"></span>NOVACLAD</div>
    <div class="details">
      FULL NAME<br>The Job Title<br>email@novaclad.com<br>01234567890
      <div class="gap"></div>
      01234567890<br>1 Street Address<br>Yourcity<br>1234
    </div>
    <div class="web">www.novaclad.com</div>
    <div class="edge-band"></div>
  </section>

  <section class="card card-back" aria-label="Business card back">
    <ul class="products">
      <li>Zinc</li>
      <li>Copper</li>
      <li>Titanium</li>
      <li>Stainless Steel</li>
      <li>CFC (Pre-finished &amp; standard)</li>
      <li>Aluminium (composite &amp; solid)</li>
    </ul>
    <div class="edge-band"></div>
  </section>

</main>
</body>
</html>
```